Design a Mobile App for Landscape Businesses

This project is to design the first three screens for a mobile app for Landscape and Lawncare businesses. This app will serve as a directory for homeowners to locate landscape and lawn care businesses and for landscape businesses and contractors to run their business. See the attached PDF for more information and example
Here is the link to the description https://brevlinq.test/k3r92P

Target Market(s)

Landscape and lawn care business, gardeners, home owners

Industry/Entity Type

Landscape Gardening

Logo Text

Quillmoray

Colors

Designer to choose colors to be used in the design.

```html
<!DOCTYPE html>
<html lang="en">
<head>
<meta charset="utf-8">
<title>Quillmoray</title>
<link rel="stylesheet" href="https://fonts.googleapis.com/css2?family=Roboto:wght@300;400;500;700&display=swap">
<style>
:root{
  --bg:#e4e6ea;
  --screen:#ffffff;
  --ink:#1f2328;
  --muted:#8a8f96;
  --line:#e3e6ea;
  --green:#22c55e;
  --star:#f97316;
  --icon-grey:#b9bec4;
}
*{box-sizing:border-box;margin:0;padding:0}
html,body{width:1200px;height:865px;overflow:hidden;background:var(--bg);font-family:"Roboto",sans-serif;color:var(--ink)}
.canvas{position:relative;width:1200px;height:865px}
.brand{position:absolute;right:60px;top:52px;display:flex;align-items:center;gap:14px}
.brand-dot{width:18px;height:18px;border-radius:50%;background:var(--green)}
.brand-name{font-weight:300;font-size:48px;color:var(--ink);letter-spacing:-0.5px}
.screen{position:absolute;top:170px;width:330px;height:640px;background:var(--screen);border-radius:18px;overflow:hidden;box-shadow:0 20px 40px rgba(0,0,0,.08)}
.screen-list{left:60px}
.screen-profile{left:435px}
.screen-settings{left:810px}
.menu{position:absolute;right:20px;top:22px}
.photo{background:linear-gradient(135deg,#9bd34a,#2f7d2b 55%,#173f1c)}
.photo-lawn{background:linear-gradient(160deg,#1d3b1a,#3f8f2f 60%,#a6d86b)}
.photo-path{background:linear-gradient(135deg,#d8d3c8,#8bb15d 55%,#3e7c2a)}
.photo-leaves{background:linear-gradient(135deg,#cfe6b8,#4f9a3c 50%,#1f4a22)}
.photo-aerial{background:linear-gradient(135deg,#7cb84a,#cfc5a5 50%,#4a8a32)}
.btn{display:inline-block;background:var(--green);color:#fff;font-size:9px;font-weight:500;border-radius:12px;padding:5px 14px}
.badge{display:inline-block;background:var(--green);color:#fff;font-size:7px;border-radius:6px;padding:2px 6px;vertical-align:middle;margin-left:4px}
.stars{color:var(--star);font-size:9px;letter-spacing:1px}
.count{color:var(--muted);font-size:8px;margin-left:3px}
.meta{font-size:8px;color:var(--muted)}
.addr{font-size:8px;font-weight:500;line-height:1.3}
.icons{display:flex;gap:8px}
.ic{width:18px;height:18px;border-radius:50%;display:flex;align-items:center;justify-content:center}
.ic.on{background:var(--green)}
.ic.off{background:var(--icon-grey)}
.search{position:absolute;left:20px;right:20px;top:60px;padding-bottom:8px;border-bottom:1px solid var(--green);font-size:11px;display:flex;gap:8px;align-items:center}
.search .hint{color:var(--muted)}
.results{position:absolute;left:20px;right:20px;top:100px}
.result{display:flex;gap:12px;position:relative;height:128px}
.thumb{width:80px;height:60px;flex:none;border-radius:2px}
.result-name{font-size:13px;font-weight:500}
.result .dist{position:absolute;right:0;top:0;font-size:8px;color:var(--muted)}
.result .icons{position:absolute;right:0;top:20px}
.result-body{display:flex;flex-direction:column;gap:4px}
.hero{position:absolute;left:0;top:0;width:330px;height:260px}
.hero-bar{position:absolute;left:0;right:0;top:18px;display:flex;justify-content:space-between;align-items:center;padding:0 20px;color:#fff;font-size:13px}
.dots{position:absolute;right:20px;top:230px;display:flex;gap:4px}
.dots span{width:5px;height:5px;border-radius:50%;background:rgba(255,255,255,.6)}
.dots span.on{background:var(--green)}
.profile-thumb{position:absolute;left:20px;top:220px;width:90px;height:70px}
.profile-info{position:absolute;left:125px;right:20px;top:270px;display:flex;flex-direction:column;gap:5px}
.profile-name{font-size:17px;font-weight:500}
.desc{font-size:8px;color:var(--muted);line-height:1.4}
.profile-icons{position:absolute;left:20px;top:305px}
.services{position:absolute;left:20px;right:20px;top:470px}
.services h2{font-size:18px;font-weight:500;margin-bottom:6px}
.services p{font-size:9px;font-weight:500;line-height:1.4}
.back{position:absolute;left:20px;top:22px}
.settings-title{position:absolute;left:0;right:0;top:80px;text-align:center;font-size:14px;font-weight:500}
.avatar{position:absolute;left:120px;top:130px;width:90px;height:70px}
.avatar-btn{position:absolute;left:135px;top:195px}
.rows{position:absolute;left:30px;right:30px;top:260px}
.row{display:flex;justify-content:space-between;padding:14px 0;border-bottom:1px solid var(--line);font-size:11px;color:#555}
.save{position:absolute;left:60px;right:60px;top:560px;text-align:center;padding:9px;font-size:11px;border-radius:16px}
</style>
</head>
<body>
<div class="canvas">
  <header class="brand">
    <span class="brand-dot"></span>
    <span class="brand-name">Quillmoray</span>
  </header>

  <section class="screen screen-list">
    <svg class="menu" width="20" height="10"><path d="M0 1h20M4 8h16" stroke="#222" stroke-width="2"/></svg>
    <div class="search">
      <svg width="10" height="10"><circle cx="4" cy="4" r="3" fill="none" stroke="#999" stroke-width="1.4"/><path d="M6.5 6.5l3 3" stroke="#999" stroke-width="1.4"/></svg>
      <span>Find</span><span class="hint">service, nearby</span>
    </div>
    <div class="results">
      <article class="result">
        <div class="thumb photo-lawn" role="img" aria-label="Mown lawn with a garden path"></div>
        <div class="result-body">
          <div class="result-name">Fernbrook Lawns<span class="badge">Sponsor</span></div>
          <div><span class="stars">★★★★★</span><span class="count">(23)</span></div>
          <div class="meta">Indoor, Outdoor Landscaping and more</div>
          <div class="addr">14 Larkspur Row,<br>Eastmere EM4 2QT</div>
          <div><span class="btn">Request a Quote</span></div>
        </div>
        <span class="dist">2.1 mi</span>
        <div class="icons">
          <span class="ic on"><svg width="9" height="9"><path d="M2 1l2 2-1 1.5a5 5 0 0 0 2 2L6.5 5l2 2-1.5 1.5C4 8 1 5 .5 1.5z" fill="#fff"/></svg></span>
          <span class="ic off"><svg width="9" height="7"><rect x=".5" y=".5" width="8" height="6" fill="none" stroke="#fff"/><path d="M.5.5l4 3 4-3" fill="none" stroke="#fff"/></svg></span>
          <span class="ic on"><svg width="9" height="9"><circle cx="2" cy="4.5" r="1.3" fill="#fff"/><circle cx="7" cy="2" r="1.3" fill="#fff"/><circle cx="7" cy="7" r="1.3" fill="#fff"/><path d="M2 4.5L7 2M2 4.5L7 7" stroke="#fff"/></svg></span>
        </div>
      </article>
      <article class="result">
        <div class="thumb photo-path" role="img" aria-label="Stone path beside a green hedge"></div>
        <div class="result-body">
          <div class="result-name">Mossgate</div>
          <div><span class="stars">★★★★☆</span><span class="count">(15)</span></div>
          <div class="meta">Landscaping and Interior Design</div>
          <div class="addr">88 Willowbank Lane,<br>Eastmere EM2 7LP</div>
          <div><span class="btn">Request a Quote</span></div>
        </div>
        <span class="dist">3.6 mi</span>
        <div class="icons">
          <span class="ic on"><svg width="9" height="9"><path d="M2 1l2 2-1 1.5a5 5 0 0 0 2 2L6.5 5l2 2-1.5 1.5C4 8 1 5 .5 1.5z" fill="#fff"/></svg></span>
          <span class="ic on"><svg width="9" height="7"><rect x=".5" y=".5" width="8" height="6" fill="none" stroke="#fff"/><path d="M.5.5l4 3 4-3" fill="none" stroke="#fff"/></svg></span>
          <span class="ic on"><svg width="9" height="9"><circle cx="2" cy="4.5" r="1.3" fill="#fff"/><circle cx="7" cy="2" r="1.3" fill="#fff"/><circle cx="7" cy="7" r="1.3" fill="#fff"/><path d="M2 4.5L7 2M2 4.5L7 7" stroke="#fff"/></svg></span>
        </div>
      </article>
      <article class="result">
        <div class="thumb photo-leaves" role="img" aria-label="Tall green plant leaves"></div>
        <div class="result-body">
          <div class="result-name">Hedgecraft</div>
          <div><span class="stars">★★★★☆</span><span class="count">(09)</span></div>
          <div class="meta">Landscaping and Interior Design</div>
          <div class="addr">6 Thornfield Court,<br>Ashby Road EM9</div>
          <div><span class="btn">Request a Quote</span></div>
        </div>
        <span class="dist">5.8 mi</span>
        <div class="icons">
          <span class="ic off"><svg width="9" height="9"><path d="M2 1l2 2-1 1.5a5 5 0 0 0 2 2L6.5 5l2 2-1.5 1.5C4 8 1 5 .5 1.5z" fill="#fff"/></svg></span>
          <span class="ic off"><svg width="9" height="7"><rect x=".5" y=".5" width="8" height="6" fill="none" stroke="#fff"/><path d="M.5.5l4 3 4-3" fill="none" stroke="#fff"/></svg></span>
          <span class="ic off"><svg width="9" height="9"><circle cx="2" cy="4.5" r="1.3" fill="#fff"/><circle cx="7" cy="2" r="1.3" fill="#fff"/><circle cx="7" cy="7" r="1.3" fill="#fff"/><path d="M2 4.5L7 2M2 4.5L7 7" stroke="#fff"/></svg></span>
        </div>
      </article>
      <article class="result">
        <div class="thumb photo-aerial" role="img" aria-label="Aerial view of a landscaped garden"></div>
        <div class="result-body">
          <div class="result-name">Bloomfield Yards</div>
          <div><span class="stars">★★★★☆</span><span class="count">(09)</span></div>
          <div class="meta">Landscaping and Interior Design</div>
          <div class="addr">21 Orchard Hall, Copse Street EM3</div>
          <div><span class="btn">Request a Quote</span></div>
        </div>
        <span class="dist">4.8 mi</span>
      </article>
    </div>
  </section>

  <section class="screen screen-profile">
    <div class="hero photo" role="img" aria-label="Close-up of green garden plant shoots"></div>
    <div class="hero-bar">
      <svg width="18" height="10"><path d="M1 5h16M5 1L1 5l4 4" fill="none" stroke="#fff" stroke-width="1.5"/></svg>
      <span>Profile</span>
      <span style="display:flex;gap:18px;align-items:center">
        <svg width="16" height="14"><path d="M8 13S1 8.5 1 4.5A3.5 3.5 0 0 1 8 3a3.5 3.5 0 0 1 7 1.5C15 8.5 8 13 8 13z" fill="none" stroke="#fff" stroke-width="1.4"/></svg>
        <svg width="20" height="10"><path d="M0 1h20M4 8h16" stroke="#fff" stroke-width="2"/></svg>
      </span>
    </div>
    <div class="dots"><span></span><span></span><span class="on"></span><span></span><span></span></div>
    <div class="profile-thumb photo-lawn" role="img" aria-label="Mown lawn with a garden path"></div>
    <div class="profile-info">
      <div class="profile-name">Fernbrook Lawns<span class="badge">Sponsor</span></div>
      <div><span class="stars">★★★★★</span><span class="count">(23)</span></div>
      <p class="desc">Family-run crew offering lawn mowing, hedge shaping, planting and seasonal care across the city. Friendly quotes, tidy work and reliable weekly visits for every garden.</p>
      <div class="addr">14 Larkspur Row,<br>Eastmere EM4 2QT</div>
      <div><span class="btn">Request a Quote</span></div>
    </div>
    <div class="icons profile-icons">
      <span class="ic on"><svg width="9" height="9"><path d="M2 1l2 2-1 1.5a5 5 0 0 0 2 2L6.5 5l2 2-1.5 1.5C4 8 1 5 .5 1.5z" fill="#fff"/></svg></span>
      <span class="ic off"><svg width="9" height="7"><rect x=".5" y=".5" width="8" height="6" fill="none" stroke="#fff"/><path d="M.5.5l4 3 4-3" fill="none" stroke="#fff"/></svg></span>
      <span class="ic on"><svg width="9" height="9"><circle cx="2" cy="4.5" r="1.3" fill="#fff"/><circle cx="7" cy="2" r="1.3" fill="#fff"/><circle cx="7" cy="7" r="1.3" fill="#fff"/><path d="M2 4.5L7 2M2 4.5L7 7" stroke="#fff"/></svg></span>
    </div>
    <div class="services">
      <h2>List of services</h2>
      <p>Pre-Emergents, Post-Emergents, Fertilization, Mowing<br>Watering, Aeration, Dethatching</p>
    </div>
  </section>

  <section class="screen screen-settings">
    <svg class="back" width="18" height="10"><path d="M1 5h16M5 1L1 5l4 4" fill="none" stroke="#222" stroke-width="1.5"/></svg>
    <svg class="menu" width="20" height="10"><path d="M0 1h20M4 8h16" stroke="#222" stroke-width="2"/></svg>
    <h1 class="settings-title">Account Settings</h1>
    <div class="avatar photo-lawn" role="img" aria-label="Account picture of a mown lawn"></div>
    <span class="btn avatar-btn">Change</span>
    <div class="rows">
      <div class="row"><span>Profile</span><span>›</span></div>
      <div class="row"><span>Password</span><span>›</span></div>
      <div class="row"><span>Email Address</span><span>›</span></div>
      <div class="row"><span>Location</span><span>›</span></div>
      <div class="row"><span>Privacy Settings</span><span>›</span></div>
    </div>
    <span class="btn save">Save</span>
  </section>
</div>
</body>
</html>
```